Aesthetic shopify website with functioning mobile version

I need a website that looks aesthetically pleasing using the pictures, logos, and product that I provide in the files. I also need to have an aesthetic easy to use mobile version as well.

Here is a list of things I want included in the website.
- Shipping rates are surfaced during checkout
- Discount codes can be applied in the cart
- A shopper can edit their cart’s content
- There is an option for order status tracking
- An email notification is sent to confirm a purchase

The domain is www.brimvantel.com, so I am not sure how to go forward with having you convert it to that domain. I look forward to working with you!

```html
<!DOCTYPE html>
<html lang="en">
<head>
<meta charset="utf-8">
<title>Brimvantel — Curl Defining Cream</title>
<link href="https://fonts.googleapis.com/css2?family=Lato:wght@400;700;900&family=Roboto:wght@500;700&display=swap" rel="stylesheet">
<style>
:root{
  --gold:#7a6640;
  --gold-light:#b79a5b;
  --ink:#222222;
  --text:#333333;
  --paper:#ffffff;
  --mist:#f1f1f1;
  --night:#1f1f1f;
  --olive-dark:#2e2e28;
  --star:#e0a826;
}
*{margin:0;padding:0;box-sizing:border-box}
html,body{width:1200px;height:2642px;overflow:hidden}
body{position:relative;font-family:"Lato",sans-serif;color:var(--text);background:var(--paper)}
.abs{position:absolute}

/* hero */
.hero{left:0;top:0;width:1200px;height:680px;background:linear-gradient(100deg,#4d544c 0%,#545b52 45%,#6a5c4d 72%,#7b6b5c 100%)}
.hero-tube{left:204px;top:240px;width:266px;height:447px;background:linear-gradient(90deg,#1c1c1c,#303030 50%,#1c1c1c);clip-path:polygon(0 0,100% 0,82% 82%,80% 100%,20% 100%,18% 82%)}
.logo{left:74px;top:34px;font-family:"Lato",sans-serif;font-weight:900;font-size:38px;letter-spacing:1px;color:var(--paper);display:flex;align-items:center;gap:10px}
.logo .dot{width:10px;height:10px;border-radius:50%;background:var(--paper)}
.nav{left:437px;top:48px;display:flex;gap:0}
.nav a{display:block;height:31px;line-height:31px;padding:0 14px;font-size:11.5px;font-weight:700;color:var(--paper);text-decoration:none;text-transform:uppercase;letter-spacing:.2px}
.nav a.active{background:var(--gold);padding:0 13px}
.tools{left:1056px;top:55px;display:flex;gap:12px;align-items:center;color:var(--paper);font-size:11px;font-weight:700}
.arrow{top:318px;width:46px;height:46px;border-radius:50%;background:rgba(255,255,255,.25);display:flex;align-items:center;justify-content:center}

/* section headings */
.heading{left:0;width:1200px;text-align:center;font-weight:900;font-size:31px;color:var(--ink);letter-spacing:.3px}
.rule{left:555px;width:90px;height:3px;background:var(--gold)}
.rule.light{background:var(--paper)}

/* ingredients */
.ing{font-size:13.5px;line-height:23.5px;color:var(--ink)}
.ing-center{left:400px;top:878px;width:400px;text-align:center}
.ing-left{left:268px;top:1162px;width:210px;text-align:right}
.ing-right{left:704px;top:1159px;width:230px}
.mid-tube{left:522px;top:975px;width:154px;height:310px;background:linear-gradient(180deg,#262626 0%,#1d1d1d 78%,rgba(200,200,200,.2) 100%);clip-path:polygon(0 0,100% 0,82% 80%,80% 96%,20% 96%,18% 80%)}

/* featured */
.featured{left:0;top:1322px;width:1200px;height:727px;background:var(--mist)}
.gallery{left:165px;top:1502px;width:405px;height:383px;background:var(--paper)}
.gallery-tube{left:283px;top:1548px;width:168px;height:300px;background:linear-gradient(90deg,#1c1c1c,#333 50%,#1c1c1c);clip-path:polygon(0 0,100% 0,82% 84%,80% 100%,20% 100%,18% 84%)}
.thumb{top:1895px;width:88px;height:87px;background:var(--paper);display:flex;align-items:center;justify-content:center}
.thumb span{display:block;width:28px;height:62px;background:#222;clip-path:polygon(0 0,100% 0,80% 85%,75% 100%,25% 100%,20% 85%)}
.p-name{left:597px;top:1515px;font-family:"Roboto",sans-serif;font-weight:700;font-size:27px;color:var(--ink)}
.p-rating{left:599px;top:1553px;display:flex;align-items:center;gap:6px;font-size:10px;font-weight:700;color:var(--ink)}
.p-price{left:599px;top:1575px;font-size:11px;font-weight:700;color:var(--ink)}
.p-price s{margin-right:4px}
.p-divider{left:599px;top:1604px;width:378px;height:1px;background:#e2e2e2}
.p-desc{left:599px;top:1618px;width:420px;font-size:13.2px;line-height:23.4px;color:var(--text)}
.p-qlabel{left:598px;top:1758px;font-size:11px;font-weight:700;color:var(--ink)}
.qty{left:599px;top:1777px;width:206px;height:46px;border:2px solid var(--ink);display:flex;background:var(--paper)}
.qty div{display:flex;align-items:center;justify-content:center;font-size:14px;color:var(--ink)}
.qty .btn{width:56px;font-size:22px;font-weight:900}
.qty .val{flex:1;border-left:2px solid var(--ink);border-right:2px solid var(--ink)}
.add{left:813px;top:1777px;width:206px;height:46px;background:#000;color:var(--paper);display:flex;align-items:center;justify-content:center;gap:8px;font-family:"Roboto",sans-serif;font-weight:500;font-size:14.5px;letter-spacing:.4px}
.buy{left:601px;top:1832px;width:418px;height:52px;background:var(--olive-dark);color:var(--paper);display:flex;align-items:center;justify-content:center;font-family:"Roboto",sans-serif;font-weight:700;font-size:19px;letter-spacing:.3px}

/* email band */
.band{left:0;top:2049px;width:1200px;height:289px;background:var(--gold)}
.band-photo{left:0;top:2049px;width:300px;height:289px;background:linear-gradient(90deg,#e7d7c6 0%,#c9a37f 40%,rgba(122,102,64,0) 100%)}
.band-tube{left:940px;top:2070px;width:240px;height:268px;background:linear-gradient(90deg,#1d1d1d,#2f2f2f 55%,#1d1d1d);clip-path:polygon(12% 0,100% 15%,72% 100%,0 100%)}
.band-title{left:0;top:2096px;width:1200px;text-align:center;color:var(--paper);font-weight:900;font-size:39px;letter-spacing:.5px}
.band-sub{left:0;top:2188px;width:1200px;text-align:center;color:var(--paper);font-size:18.5px;letter-spacing:.3px}
.field{background:var(--paper);font-size:11.5px;color:#444;padding-left:12px;display:flex;align-items:center}
.band-input{left:340px;top:2238px;width:403px;height:45px}
.band-btn{left:757px;top:2238px;width:103px;height:45px;background:#000;color:var(--paper);display:flex;align-items:center;justify-content:center;font-family:"Roboto",sans-serif;font-weight:700;font-size:14px}

/* footer */
.footer{left:0;top:2338px;width:1200px;height:304px;background:var(--night)}
.f-links{left:77px;top:2405px;display:flex;gap:39px;color:var(--paper);font-weight:900;font-size:15.5px}
.f-copy{left:79px;top:2460px;color:var(--paper);font-size:15px;line-height:27px}
.cards{left:79px;top:2540px;display:flex;gap:11px}
.cards span{display:block;width:42px;height:26px;border-radius:3px}
.f-news{left:616px;top:2405px;color:var(--paper);font-weight:900;font-size:15.5px}
.f-news-sub{left:616px;top:2441px;color:var(--paper);font-size:15px}
.f-first{left:616px;top:2479px;width:248px;height:43px}
.f-last{left:878px;top:2479px;width:248px;height:43px}
.f-email{left:616px;top:2531px;width:403px;height:43px}
.f-btn{left:1027px;top:2531px;width:99px;height:43px;background:var(--gold);color:var(--paper);display:flex;align-items:center;justify-content:center;font-weight:900;font-size:13px}
</style>
</head>
<body>

<!-- hero -->
<div class="abs hero" role="img" aria-label="Photo of a man with curly hair and a beard in a home setting"></div>
<div class="abs hero-tube" role="img" aria-label="Curl defining cream tube"></div>
<div class="abs logo"><span>BRIMVANTEL</span><span class="dot"></span></div>
<nav class="abs nav">
  <a class="active">Home</a><a>About Us</a><a>Products</a><a>Ingredients</a><a>Reviews</a><a>Contact Us</a>
</nav>
<div class="abs tools">
  <svg width="11" height="11" viewBox="0 0 12 12"><circle cx="5" cy="5" r="3.8" fill="none" stroke="#fff" stroke-width="1.8"/><line x1="8" y1="8" x2="11" y2="11" stroke="#fff" stroke-width="2"/></svg>
  <svg width="10" height="11" viewBox="0 0 10 11"><circle cx="5" cy="3" r="2.6" fill="#fff"/><path d="M0 11 Q5 3 10 11Z" fill="#fff"/></svg>
  <span style="display:flex;gap:3px;align-items:center"><svg width="13" height="11" viewBox="0 0 13 11"><path d="M0 1h2l2 7h7l2-5H3" fill="none" stroke="#fff" stroke-width="1.6"/><circle cx="5" cy="10" r="1" fill="#fff"/><circle cx="10" cy="10" r="1" fill="#fff"/></svg>0</span>
</div>
<div class="abs arrow" style="left:31px"><svg width="18" height="22" viewBox="0 0 18 22"><path d="M13 2 4 11l9 9" fill="none" stroke="#333" stroke-width="4"/></svg></div>
<div class="abs arrow" style="left:1128px"><svg width="18" height="22" viewBox="0 0 18 22"><path d="M5 2l9 9-9 9" fill="none" stroke="#333" stroke-width="4"/></svg></div>

<!-- key ingredients -->
<h2 class="abs heading" style="top:740px">KEY INGREDIENTS</h2>
<div class="abs rule" style="top:799px"></div>
<svg class="abs" style="left:580px;top:830px" width="40" height="40" viewBox="0 0 40 40" fill="none" stroke="#b79a5b" stroke-width="1.5"><path d="M20 4c-6 10 6 14 0 24"/><circle cx="12" cy="30" r="6"/><circle cx="27" cy="30" r="6"/><path d="M10 22c-2-4 0-8 4-9"/></svg>
<p class="abs ing ing-center">Helianthus Annuus (Sunflower) Extract - Naturally-derived UV protectant for hair to&nbsp; prevent color fading, while also conditioning hair and adding shine</p>
<div class="abs mid-tube" role="img" aria-label="Curl defining cream tube"></div>
<svg class="abs" style="left:436px;top:1114px" width="42" height="40" viewBox="0 0 42 40" fill="none" stroke="#b79a5b" stroke-width="1.5"><rect x="6" y="2" width="10" height="7"/><rect x="2" y="9" width="18" height="28" rx="2"/><line x1="2" y1="22" x2="20" y2="22"/><circle cx="32" cy="30" r="7"/><circle cx="32" cy="18" r="5"/></svg>
<p class="abs ing ing-left">Simmondsia Chinensis (Jojoba) Seed Oil - Deep penetrating oil that softens and conditions</p>
<svg class="abs" style="left:704px;top:1114px" width="40" height="40" viewBox="0 0 40 40" fill="none" stroke="#b79a5b" stroke-width="1.5"><circle cx="20" cy="20" r="5"/><circle cx="34" cy="5" r="3"/><circle cx="6" cy="8" r="3"/><circle cx="6" cy="34" r="3"/><circle cx="34" cy="32" r="3"/><path d="M24 17l8-10M16 17 8 10M16 23l-8 9M24 23l8 7"/></svg>
<p class="abs ing ing-right">Polyquaternium-11 - Plant- derived polymer to add volume and help thicken hai</p>

<!-- featured products -->
<section class="abs featured"></section>
<h2 class="abs heading" style="top:1383px">FEATURED PRODUCTS</h2>
<div class="abs rule" style="top:1443px"></div>
<div class="abs gallery"></div>
<div class="abs gallery-tube" role="img" aria-label="Curl defining cream tube"></div>
<div class="abs thumb" style="left:218px"><span></span></div>
<div class="abs thumb" style="left:324px"><span></span></div>
<div class="abs thumb" style="left:430px"><span></span></div>

<h3 class="abs p-name">BRIMVANTEL</h3>
<div class="abs p-rating">
  <svg width="58" height="10" viewBox="0 0 58 10"><g fill="#e0a826"><path id="s" d="M5 0l1.5 3.3 3.5.4-2.6 2.4.7 3.5L5 7.9 1.9 9.6l.7-3.5L0 3.7l3.5-.4z"/><use href="#s" x="12"/><use href="#s" x="24"/><use href="#s" x="36"/><use href="#s" x="48"/></g></svg>
  <span>25 reviews</span>
</div>
<div class="abs p-price"><s>$150.00</s>$110.00</div>
<div class="abs p-divider"></div>
<p class="abs p-desc">On the other hand, we denounce with righteous indignation and dislike men who are so beguiled and demoralized by the charms of pleasure of the moment, so blinded by desire, that they cannot foresee the pain and trouble that are bound to ensue; and equal blame belongs to those who fail in their duty through weakness.</p>
<div class="abs p-qlabel">Quantity</div>
<div class="abs qty"><div class="btn">+</div><div class="val">1</div><div class="btn">−</div></div>
<div class="abs add">
  <svg width="15" height="13" viewBox="0 0 15 13"><path d="M0 1h2.5l2 8h8l2-6H4" fill="#fff" stroke="#fff" stroke-width="1.4"/><circle cx="6" cy="11.5" r="1.3" fill="#fff"/><circle cx="11.5" cy="11.5" r="1.3" fill="#fff"/></svg>
  ADD TO CART
</div>
<div class="abs buy">BUY NOW</div>

<!-- email band -->
<section class="abs band"></section>
<div class="abs band-photo" role="img" aria-label="Photo of a smiling woman with long curly hair pointing toward the form"></div>
<div class="abs band-tube" role="img" aria-label="Curl defining cream tube"></div>
<h2 class="abs band-title">JOIN EMAIL LISTING</h2>
<div class="abs rule light" style="top:2165px"></div>
<p class="abs band-sub">Be the first to hear about new products and community events</p>
<div class="abs field band-input">Email Address</div>
<div class="abs band-btn">SIGN UP</div>

<!-- footer -->
<footer class="abs footer"></footer>
<div class="abs f-links"><span>ABOUT US</span><span>CONTACT US</span><span>SEARCH</span></div>
<p class="abs f-copy">Copyright © 2021. CompanyName<br>All Right Reserved</p>
<div class="abs cards">
  <span style="background:#fff"></span><span style="background:#fff"></span><span style="background:#2e6fc0"></span><span style="background:#fff"></span><span style="background:#fff"></span><span style="background:#f3efe6"></span>
</div>
<h4 class="abs f-news">NEWSLETTER SIGN UP</h4>
<p class="abs f-news-sub">Sign up or our newsletter below to keep in touch with our community</p>
<div class="abs field f-first">First Name</div>
<div class="abs field f-last">Last Name</div>
<div class="abs field f-email">Email Address</div>
<div class="abs f-btn">SIGN UP</div>

</body>
</html>
```